Equipment Finance Specialist I work with companies who need the funds to buy their equipment

I would like a business card that stands out on the shelves. I want to be able to hand it to someone and say WOW. This card should have my logo.
You can put color into it I am very open on design and color

What my company does is we deal with dealerships that sell equipment such as Dump Trucks garbage trucks tractors trailers. Customers get referred to us and depending on their time in business we will ask for the following items

Companies that have been in business for more than two years we have a credit application program up to 250K . With this program we need the following items Credit application filled out(which is what I would like to be able for the customer to click on my website to get.) as well as three current month bank statements.

Deals over 250k we will need the following items

2 years business tax returns
2 years personal tax returns
Profit & Loss statement
Personal Financial Statement

what we do
100% FINANCING
SEASONAL PAYMENTS
LOAN BALLOON PAYMENTS
TRAC LEASING
LOW-INTEREST REFINANCING RATES
DEBT CONSOLIDATION

We specialize in creative financing solutions and offer a variety of reliable, flexible and expandable lending choices.

Target Market(s)

Trucking Companies

Industry/Entity Type

Trucking Company

Contact Information for Business Card

* $250,000 Application only Program
* Loans from $30,000 to 5,000,000
* Competitive Interest Rates

Font styles to use
Serif
Sans Serif

Colors

Designer to choose colors to be used in the design.

Requirements
Must have
• On the back of the card.
• * $250,000 Application only Program
• * Loans from $30,000 to 5,000,000
• My name, email, website. address
• * Competitive Interest Rates
• * 100% Financing
Nice to have
• I want my logo to pop on the card
• My logo is the great one I would like to use
Should not have
• I am up for your creativity as well

```html
<!DOCTYPE html>
<html lang="en">
<head>
<meta charset="utf-8">
<title>Summit Lending – Business Card</title>
<link href="https://fonts.googleapis.com/css2?family=Open+Sans:wght@400;600;700;800&display=swap" rel="stylesheet">
<style>
  :root {
    --navy: #0d2a6b;
    --red: #c8102e;
    --white: #ffffff;
    --ink: #1f2a44;
    --muted: #cfd6e6;
    --bg: #d9d9d9;
  }
  * { box-sizing: border-box; margin: 0; padding: 0; }
  html, body { width: 1200px; height: 900px; overflow: hidden; }
  body {
    background: var(--bg);
    font-family: "Open Sans", Arial, sans-serif;
    position: relative;
  }
  .card {
    position: absolute;
    width: 540px;
    height: 310px;
    border-radius: 26px;
    overflow: hidden;
    box-shadow: 0 10px 24px rgba(0,0,0,0.18);
  }

  .brand {
    display: flex; align-items: center; gap: 10px;
    font-weight: 800; letter-spacing: 1px; text-transform: uppercase;
    white-space: nowrap;
  }
  .brand__dot { width: 22px; height: 22px; border-radius: 50%; background: currentColor; flex: none; }

  /* Services side */
  .card--services {
    left: 80px; top: 110px;
    background: var(--navy);
    color: var(--white);
    text-align: center;
  }
  .card--services .brand {
    justify-content: center; margin-top: 46px;
    font-size: 32px; color: var(--white);
  }
  .services__rule { height: 1px; background: rgba(255,255,255,0.35); margin: 12px 40px 8px; }
  .services__heading { font-weight: 700; font-size: 13px; letter-spacing: 1px; margin-bottom: 2px; }
  .services__list { font-size: 12.5px; line-height: 1.5; letter-spacing: 0.4px; text-transform: uppercase; color: var(--muted); white-space: nowrap; }
  .services__list span + span::before { content: "•"; margin: 0 8px; color: var(--white); }
  .requirements {
    position: absolute; left: 0; right: 0; bottom: 0; height: 74px;
    background: var(--red);
    display: flex; flex-direction: column; justify-content: center;
    font-size: 14.5px; line-height: 1.45;
  }

  /* Contact side */
  .card--contact {
    left: 580px; top: 480px;
    background: var(--white);
    color: var(--ink);
  }
  .card--contact .brand {
    position: absolute; left: 36px; top: 36px;
    font-size: 30px; color: var(--navy);
  }
  .person { position: absolute; left: 40px; top: 112px; }
  .person__name { font-size: 20px; font-weight: 800; color: var(--navy); text-transform: uppercase; white-space: nowrap; }
  .person__name em { font-style: normal; color: var(--red); }
  .person__role { font-size: 14px; margin-bottom: 8px; }
  .contact-list { list-style: none; font-size: 14px; line-height: 1.6; }
  .contact-list li { display: flex; align-items: center; gap: 8px; white-space: nowrap; }
  .contact-list svg { width: 13px; height: 13px; fill: var(--navy); flex: none; }
  .offers {
    position: absolute; left: 282px; top: 112px;
    list-style: none; font-size: 13.5px; line-height: 1.6;
  }
  .offers li { display: flex; align-items: center; gap: 8px; white-space: nowrap; }
  .offers li::before { content: ""; width: 8px; height: 8px; border-radius: 50%; background: var(--red); flex: none; }
  .address {
    position: absolute; left: 0; right: 0; bottom: 0; height: 50px;
    background: var(--navy); color: var(--white);
    display: flex; align-items: center; padding-left: 40px;
    font-size: 14px; white-space: nowrap;
  }
</style>
</head>
<body>

<section class="card card--services">
  <div class="brand"><span class="brand__dot"></span>Summit Lending</div>
  <div class="services__rule"></div>
  <h2 class="services__heading">WHAT WE DO</h2>
  <div class="services__list">
    <div><span>100% Financing</span><span>Seasonal Payments</span><span>Loan Balloon Payments</span></div>
    <div><span>TRAC Leasing</span><span>Low-Interest Refinancing Rates</span><span>Debt Consolidation</span></div>
  </div>
  <div class="services__rule"></div>
  <div class="requirements">
    <div>2 years business tax returns | 2 years personal tax returns</div>
    <div>Profit &amp; Loss statement | Personal Financial Statement</div>
  </div>
</section>

<section class="card card--contact">
  <div class="brand"><span class="brand__dot"></span>Summit Lending</div>

  <ul class="offers">
    <li>$250,000 Application only Program</li>
    <li>Loans from $30,000 to 5,000,000</li>
    <li>Competitive Interest Rates</li>
    <li>100% Financing</li>
  </ul>

  <div class="person">
    <div class="person__name">Daniel <em>Mercer</em></div>
    <div class="person__role">Managing Director</div>
    <ul class="contact-list">
      <li><svg viewBox="0 0 24 24" aria-hidden="true"><path d="M6.6 10.8a15 15 0 0 0 6.6 6.6l2.2-2.2c.3-.3.7-.4 1-.2 1.1.4 2.3.6 3.6.6.6 0 1 .4 1 1V20c0 .6-.4 1-1 1A17 17 0 0 1 3 4c0-.6.4-1 1-1h3.5c.6 0 1 .4 1 1 0 1.3.2 2.5.6 3.6.1.3 0 .7-.2 1z"/></svg>044-555 018 240</li>
      <li><svg viewBox="0 0 24 24" aria-hidden="true"><path d="M2 5h20v14H2z M2 5l10 8 10-8" fill="none" stroke="#0d2a6b" stroke-width="2.4"/></svg>info@summitlending.com</li>
      <li><svg viewBox="0 0 24 24" aria-hidden="true"><circle cx="12" cy="12" r="10"/></svg>www.summitlending.com</li>
    </ul>
  </div>

  <div class="address">18 Harbor Road, Suite 4, Springfield 01020, USA</div>
</section>

</body>
</html>
```